Real Estate Agent needs business card design

We have logo designed already, want to have business card designed. Very interested in those smaller size business card as they look very trendy. Business name is called VORENDA REALTY

```html
<!DOCTYPE html>
<html lang="en">
<head>
<meta charset="UTF-8">
<title>Vorenda Realty – Business Card</title>
<link rel="stylesheet" href="https://fonts.googleapis.com/css2?family=Cormorant+SC:wght@500;600;700&family=Open+Sans:wght@400;600&display=swap">
<style>
  :root {
    --page-bg: #ededed;
    --card-white: #fbfbfa;
    --gold: #c9a16a;
    --gold-deep: #b8894d;
    --ink: #2b2b2b;
    --ink-soft: #4a4a4a;
    --on-gold: #ffffff;
  }
  * { box-sizing: border-box; margin: 0; padding: 0; }
  html, body { width: 1200px; height: 900px; overflow: hidden; }
  body {
    background: var(--page-bg);
    font-family: "Open Sans", Arial, sans-serif;
    position: relative;
  }
  .card {
    position: absolute;
    top: 300px;
    width: 520px;
    height: 300px;
    border-radius: 2px;
    box-shadow: 0 6px 18px rgba(0,0,0,0.10);
  }
  .card--front { left: 50px; background: var(--card-white); }
  .card--back  { left: 630px; background: var(--gold); }

  .agent {
    position: absolute;
    top: 34px;
    left: 38px;
  }
  .agent__name {
    font-family: "Cormorant SC", Georgia, serif;
    font-weight: 700;
    font-size: 22px;
    color: var(--gold-deep);
    letter-spacing: 0.5px;
    line-height: 1;
  }
  .agent__title {
    font-size: 11px;
    color: var(--ink-soft);
    margin-top: 3px;
  }

  .contact {
    position: absolute;
    top: 122px;
    left: 38px;
    list-style: none;
    font-size: 11px;
    color: var(--ink-soft);
  }
  .contact__item { display: flex; align-items: center; gap: 7px; margin-bottom: 5px; }
  .contact__icon { width: 10px; height: 10px; fill: var(--gold-deep); }

  .brand {
    position: absolute;
    right: 38px;
    text-align: right;
  }
  .card--front .brand { top: 160px; }
  .brand__name {
    font-family: "Cormorant SC", Georgia, serif;
    font-weight: 600;
    font-size: 34px;
    letter-spacing: 1.5px;
    color: var(--ink);
    line-height: 1;
  }
  .brand__address {
    margin-top: 12px;
    font-size: 12px;
    line-height: 1.35;
    color: var(--ink-soft);
  }

  .card--back .brand {
    right: auto;
    left: 0;
    width: 100%;
    top: 128px;
    text-align: center;
  }
  .card--back .brand__name { color: var(--on-gold); font-size: 38px; }
</style>
</head>
<body>
  <section class="card card--front" aria-label="Business card front">
    <div class="agent">
      <p class="agent__name">Clara Wen</p>
      <p class="agent__title">Senior Property Consultant</p>
    </div>
    <ul class="contact">
      <li class="contact__item">
        <svg class="contact__icon" viewBox="0 0 10 10" aria-hidden="true"><path d="M2 0.5 L3.6 0.5 L4.2 2.8 L3 3.6 Q4 5.9 6.4 7 L7.2 5.8 L9.5 6.4 L9.5 8 Q9.5 9.5 8 9.5 Q0.5 9 0.5 2 Q0.5 0.5 2 0.5Z"/></svg>
        <span>0412 587 903</span>
      </li>
      <li class="contact__item">
        <svg class="contact__icon" viewBox="0 0 10 10" aria-hidden="true"><circle cx="5" cy="5" r="4.5"/></svg>
        <span>www.vorendarealty.com.au</span>
      </li>
    </ul>
    <div class="brand">
      <p class="brand__name">Vorenda Realty</p>
      <p class="brand__address">12A, 48 Harbour Street,<br>Lane Cove, NSW 2066</p>
    </div>
  </section>

  <section class="card card--back" aria-label="Business card back">
    <div class="brand">
      <p class="brand__name">Vorenda Realty</p>
    </div>
  </section>
</body>
</html>
```